Redesign of Plastic Surgeon Website to fully responsive / modern feel

Hi

Our current website is out of date www.harbourlinecosmetic.org

We want a fresh / modern looking design
Needs to be fully responsive design that works extremely well on ipad and mobile device

Would like design for both full screen website and mobile

Have listed a few websites of other plastic surgeons we like
http://www.reformclinicplus.com/
http://www.doriankeelermd.com/
http://www.tarrantcontours.com/
http://www.oakdenecosmeticsurgery.com/

Menu needs to include
1. About Us
2. Procedures (see current website for example)
3. News
4. Patient Resources
5. Contact Us

We are flexible with colours / images / layout

I have uploaded a document that has some content - the face pages content is completed only

some of the procedures can have content upwards of 4000 words - total website can be large with over 40,000 words
Updates

Hi I have updated the logo for our design for the new website - this is the logo and colours we want reflected throughout the siteThanks Added Wednesday, January 13, 2016

Target Market(s)

Mainly women 20-60 85% of practice
Some men 15%

Industry/Entity Type

Plastic Surgery

Number of Pages Required

5+ page

Requirements
Must have
• We need designs for
• Homepage
• Internal pages
• 1. Landing pages for breast / body / face / non surgical main pages
• 2. Procedure pages for individual pages under each section - eg breast augmentation
• 3. About us pages - like meet the doctor, our staff, clinics
• 4. Contact page
• 5. Blog / News page
Nice to have
• See our list of websites for examples of designs we like
• Like full screen design with nice hero image
• Needs to have good to call to action messages on home page like
• Specials, procedure of the month, etc

```html
<!DOCTYPE html>
<html lang="en">
<head>
<meta charset="utf-8">
<title>Harbourline Institute of Cosmetic Surgery</title>
<link rel="stylesheet" href="https://fonts.googleapis.com/css2?family=Cinzel:wght@400;700&family=Open+Sans:wght@400;600&display=swap">
<style>
:root{
  --teal:#14a085;
  --teal-dark:#0d7e68;
  --teal-light:#2bb89b;
  --header:#2e2a29;
  --band:#332f2e;
  --footer:#252222;
  --ink:#2b2b2b;
  --body:#666;
  --line:#e4e4e4;
  --sky:#a9d7ec;
  --skin:#e2c6b6;
  --skin-deep:#c9a593;
  --white:#fff;
}
*{margin:0;padding:0;box-sizing:border-box}
html,body{width:1200px;height:2571px;overflow:hidden;background:var(--white)}
body{font-family:"Open Sans",Arial,sans-serif;color:var(--body);position:relative}
.btn{position:absolute;display:flex;align-items:center;justify-content:center;background:linear-gradient(var(--teal-light),var(--teal-dark));color:var(--white);font-family:"Cinzel",Georgia,serif;font-size:14px;letter-spacing:.5px;border-radius:3px;box-shadow:0 2px 3px rgba(0,0,0,.25)}

/* header */
.site-header{position:absolute;left:0;top:0;width:1200px;height:178px;background:var(--header);border-bottom:3px solid var(--teal)}
.brand{position:absolute;left:92px;top:24px;width:112px;color:#eee;font-family:"Cinzel",Georgia,serif;font-size:17px;line-height:25px;text-align:center}
.phone-icon{position:absolute;left:588px;top:43px;width:52px;height:52px;border:2px solid var(--teal);border-radius:50%}
.phone-text{position:absolute;left:652px;top:58px;color:#ddd;font-size:13px}
.phone-text b{color:var(--teal-light);font-weight:400;font-size:16px}
.call-btn{left:873px;top:46px;width:227px;height:42px;font-size:13px}
.nav{position:absolute;left:0;top:103px;width:1200px;height:75px;font-family:"Cinzel",Georgia,serif;font-size:13px;color:#eee}
.nav span{position:absolute;top:0;height:75px;display:flex;align-items:center;white-space:nowrap}
.nav .active{background:var(--teal);width:91px;justify-content:center}

/* hero */
.hero{position:absolute;left:0;top:181px;width:1200px;height:533px;overflow:hidden;background:linear-gradient(90deg,#c9c2bd 0%,#d8d2ce 35%,#e3e0de 60%,#ebe9e8 100%)}
.hero-photo{position:absolute;left:40px;top:-40px;width:560px;height:620px;background:radial-gradient(ellipse 48% 52% at 50% 48%,#e6cbbb 0%,#d9b9a7 40%,rgba(201,194,189,0) 100%)}
.hero-shade{position:absolute;inset:0;background:rgba(60,58,56,.22)}
.hero-title{position:absolute;right:100px;top:172px;color:#555;font-family:"Cinzel",Georgia,serif;font-size:32px;white-space:nowrap}
.hero-sub{position:absolute;right:100px;top:258px;color:#666;font-size:15px;white-space:nowrap}
.hero-btn{left:764px;top:307px;width:118px;height:42px;opacity:.85}
.contact-tab{position:absolute;left:0;top:187px;width:40px;height:158px;background:var(--teal);opacity:.75;color:#fff;font-family:"Cinzel",Georgia,serif;font-size:13px;writing-mode:vertical-rl;transform:rotate(180deg);display:flex;align-items:center;justify-content:center}
.arrow{position:absolute;top:212px}

/* modal */
.signup{position:absolute;left:338px;top:268px;width:524px;height:346px;background:#fff;border:8px solid #f1f1f1;box-shadow:0 4px 18px rgba(0,0,0,.35)}
.signup .kicker{position:absolute;left:0;top:44px;width:100%;text-align:center;color:#888;font-size:17px}
.signup h2{position:absolute;left:0;top:64px;width:100%;text-align:center;color:var(--teal);font-family:"Cinzel",Georgia,serif;font-size:30px;font-weight:700;letter-spacing:1px}
.signup .field{position:absolute;left:66px;width:376px;height:42px;border:1px solid #ddd;color:#bbb;font-size:11px;display:flex;align-items:center;justify-content:center}
.signup .close{position:absolute;left:464px;top:18px}
.subscribe{left:66px;top:232px;width:376px;height:46px;font-size:15px;letter-spacing:1px;border-radius:0}

/* intro */
.intro-title{position:absolute;left:98px;top:754px;color:var(--ink);font-family:"Cinzel",Georgia,serif;font-size:23px;line-height:34px;font-weight:400}
.intro-text{position:absolute;left:98px;top:836px;width:600px;font-size:11px;line-height:24px}
.month{position:absolute;left:722px;top:760px;width:378px;height:210px;border-left:3px solid var(--teal);padding-left:26px}
.month h3{color:var(--teal);font-family:"Cinzel",Georgia,serif;font-weight:400;font-size:14px}
.month p{font-size:11px;line-height:24px;margin-top:6px}
.month .date{color:var(--ink);font-size:12px;margin-top:12px;display:flex;align-items:center;gap:6px}
.month-btn{left:751px;top:927px;width:228px;height:43px;font-size:13px}
.rule{position:absolute;left:98px;top:1015px;width:1002px;height:1px;background:var(--line)}

/* services */
.section-title{position:absolute;left:0;top:1050px;width:1200px;text-align:center;color:var(--ink);font-family:"Cinzel",Georgia,serif;font-size:24px;font-weight:400}
.card{position:absolute;top:1113px;width:319px;height:230px;box-shadow:0 14px 10px -10px rgba(0,0,0,.25)}
.card .ph{height:190px}
.card .label{height:40px;background:var(--teal);color:#fff;font-family:"Cinzel",Georgia,serif;font-size:13px;display:flex;align-items:center;justify-content:center}

/* rejuvenation band */
.band{position:absolute;left:0;top:1403px;width:1200px;height:335px;background:linear-gradient(90deg,#fff 0%,#f4f9fc 22%,#cfe8f4 45%,var(--sky) 100%)}
.band-photo{position:absolute;left:0;top:0;width:330px;height:335px;background:radial-gradient(ellipse 70% 60% at 30% 55%,#e8cbbb 0%,#eed8cc 45%,rgba(255,255,255,0) 100%)}
.band h2{position:absolute;left:358px;top:34px;color:var(--ink);font-family:"Cinzel",Georgia,serif;font-weight:400;font-size:23px;line-height:34px}
.band ul{position:absolute;left:360px;top:110px;list-style:none;font-size:11px}
.band li{height:34px;display:flex;align-items:center;gap:10px;color:#555}
.specials{left:360px;top:249px;width:138px;height:44px;font-size:13px}

/* doctor */
.doctor-photo{position:absolute;left:70px;top:1770px;width:320px;height:393px;background:radial-gradient(ellipse 45% 55% at 50% 75%,#f6f8fa 0%,#e9eef2 55%,rgba(255,255,255,0) 100%),radial-gradient(circle at 48% 16%,#d9bcaa 0%,rgba(255,255,255,0) 14%)}
.doctor h2{position:absolute;left:440px;top:1822px;color:var(--ink);font-family:"Cinzel",Georgia,serif;font-weight:400;font-size:24px}
.doctor p{position:absolute;left:440px;top:1862px;width:660px;font-size:11px;line-height:24px}
.meet-btn{left:440px;top:2052px;width:228px;height:44px;font-size:13px}

/* partners */
.partners{position:absolute;left:0;top:2163px;width:1200px;height:140px;background:var(--band)}
.badge{position:absolute;top:48px;height:44px;border:1.5px solid #bbb}

/* footer */
.footer{position:absolute;left:0;top:2303px;width:1200px;height:268px;background:var(--footer);color:#bbb;font-size:11px}
.footer h4{position:absolute;top:38px;color:#eee;font-family:"Cinzel",Georgia,serif;font-weight:400;font-size:16px}
.footer .col{position:absolute;top:78px;line-height:24px}
.footer .divider{position:absolute;left:98px;top:194px;width:1002px;height:1px;background:#3b3737}
.copy{position:absolute;left:98px;top:222px;color:#ddd;font-family:"Cinzel",Georgia,serif;font-size:11px}
.connect{position:absolute;left:808px;top:222px;color:#ddd;font-family:"Cinzel",Georgia,serif;font-size:11px}
.social{position:absolute;top:216px;width:27px;height:27px;border-radius:50%;background:#5a5656}
.code{position:absolute;left:1164px;top:224px;color:#aaa;font-size:11px}
</style>
</head>
<body>

<header class="site-header">
  <div class="brand">Harbourline Institute of Cosmetic Surgery</div>
  <div class="phone-icon">
    <svg width="48" height="48" viewBox="0 0 48 48"><rect x="18" y="12" width="12" height="22" rx="2" fill="none" stroke="#14a085" stroke-width="2"/><circle cx="24" cy="30" r="1.3" fill="#14a085"/></svg>
  </div>
  <div class="phone-text">Phone Number : <b>02 9000 4821</b></div>
  <div class="btn call-btn">Call for Appointment</div>
  <nav class="nav">
    <span class="active" style="left:362px">Home</span>
    <span style="left:476px">About Us</span>
    <span style="left:586px">Procedures</span>
    <span style="left:715px">Patient Resources</span>
    <span style="left:889px">News / Blog</span>
    <span style="left:1020px">Contact Us</span>
  </nav>
</header>

<section class="hero">
  <div class="hero-photo" role="img" aria-label="Hero photograph of a woman with smooth skin"></div>
  <div class="hero-title">Revolutionary Plastic</div>
  <div class="hero-sub">Minimal scarring and beautiful results...</div>
  <div class="btn hero-btn">More</div>
  <div class="hero-shade"></div>
  <div class="contact-tab">Contact Us</div>
  <svg class="arrow" style="left:52px" width="20" height="100" viewBox="0 0 20 100"><path d="M18 2 L2 50 L18 98" fill="none" stroke="#aaa" stroke-width="1.5"/></svg>
  <svg class="arrow" style="left:1128px" width="20" height="100" viewBox="0 0 20 100"><path d="M2 2 L18 50 L2 98" fill="none" stroke="#aaa" stroke-width="1.5"/></svg>
</section>

<div class="signup">
  <svg class="close" width="26" height="26" viewBox="0 0 26 26"><circle cx="13" cy="13" r="12" fill="#cfe3df"/><path d="M8.5 8.5 L17.5 17.5 M17.5 8.5 L8.5 17.5" stroke="#fff" stroke-width="2.5"/></svg>
  <div class="kicker">SUBSCRIPTION FORM FOR</div>
  <h2>Newsletter Signup</h2>
  <div class="field" style="top:122px">- ENTER YOUR NAME -</div>
  <div class="field" style="top:178px">- ENTER YOUR EMAIL -</div>
  <div class="btn subscribe">Subscribe</div>
</div>

<section class="intro">
  <h1 class="intro-title">Harbourline Institute of Cosmetic Surgery<br>Your future looks beautiful.</h1>
  <p class="intro-text">You can expect beautiful results at the Harbourline Institute of Cosmetic Surgery. With expertise in facelifts, breast augmentation or breast reduction and liposuction body contouring, we offer total care at every step of your transformative journey. Dr Ashcombe is one of Australia's most eminent specialists in plastic surgery, reconstructive and aesthetic surgery, and is supported by our highly qualified, professional team. As the premier plastic surgery clinic in the city, we use only the most revolutionary techniques to minimise scarring, we help you look better, feel better and enjoy a beautiful new you...</p>
  <div class="month">
    <h3>Sed ut perspiciatis unde omnis iste natus</h3>
    <p>Sed ut perspiciatis unde omnis iste natus error sit totam aperiam, dicta sunt explicabo. Nemo enim ipsam voluptatem quia voluptas eos qui ratione voluptatem sequi nesciunt. Neque porro quisquam velit, sed quia non numquam eius modi tempora incidunt</p>
    <div class="date"><svg width="12" height="12" viewBox="0 0 12 12"><rect x="1" y="2" width="10" height="9" fill="none" stroke="#2b2b2b"/><rect x="1" y="2" width="10" height="3" fill="#2b2b2b"/></svg>20 JANUARY 2016</div>
  </div>
  <div class="btn month-btn">Procedure of the Month</div>
  <div class="rule"></div>
</section>

<section class="services">
  <h2 class="section-title">What We Do</h2>
  <div class="card" style="left:98px"><div class="ph" role="img" aria-label="Photo of a smiling woman with facial contour guide lines" style="background:radial-gradient(ellipse 40% 55% at 48% 55%,#e9cdbd 0%,#e4d6cf 55%,#dfe5ea 100%)"></div><div class="label">Face</div></div>
  <div class="card" style="left:440px"><div class="ph" role="img" aria-label="Photo of a woman's torso with body contouring marks" style="background:linear-gradient(180deg,#c9a48e 0%,#e0c1ae 55%,#f3ece8 78%,#e8d0c1 100%)"></div><div class="label">Body</div></div>
  <div class="card" style="left:782px"><div class="ph" role="img" aria-label="Photo of a woman with long blonde hair in a white top" style="background:radial-gradient(ellipse 40% 35% at 50% 62%,#f2efec 0%,#e7dcd2 45%,rgba(0,0,0,0) 70%),linear-gradient(90deg,#5a4232 0%,#c99a63 25%,#8a6a4c 50%,#c99a63 75%,#5a4232 100%)"></div><div class="label">Breast</div></div>
</section>

<section class="band">
  <div class="band-photo" role="img" aria-label="Close-up photo of a woman's face with lift arrows"></div>
  <h2>Nurture your natural beauty with the<br>rejuvenation you deserve</h2>
  <ul>
    <li><svg width="11" height="11" viewBox="0 0 11 11"><circle cx="5.5" cy="5.5" r="5.5" fill="#14a085"/><path d="M4 3 L7 5.5 L4 8" fill="none" stroke="#fff" stroke-width="1.4"/></svg>Neque porro quisquam est, qui dolorem ipsum quia dolor sit amet, consectetur, adipisci velit, sed quia non numquam eius modi tempora.</li>
    <li><svg width="11" height="11" viewBox="0 0 11 11"><circle cx="5.5" cy="5.5" r="5.5" fill="#14a085"/><path d="M4 3 L7 5.5 L4 8" fill="none" stroke="#fff" stroke-width="1.4"/></svg>Neque porro quisquam est, qui dolorem ipsum quia dolor sit amet, consectetur, adipisci velit, sed quia non numquam eius modi tempora.</li>
    <li><svg width="11" height="11" viewBox="0 0 11 11"><circle cx="5.5" cy="5.5" r="5.5" fill="#14a085"/><path d="M4 3 L7 5.5 L4 8" fill="none" stroke="#fff" stroke-width="1.4"/></svg>Neque porro quisquam est, qui dolorem ipsum quia dolor sit amet, consectetur, adipisci velit, sed quia non numquam eius modi tempora.</li>
    <li><svg width="11" height="11" viewBox="0 0 11 11"><circle cx="5.5" cy="5.5" r="5.5" fill="#14a085"/><path d="M4 3 L7 5.5 L4 8" fill="none" stroke="#fff" stroke-width="1.4"/></svg>Neque porro quisquam est, qui dolorem ipsum quia dolor sit amet, consectetur, adipisci velit, sed quia non numquam eius modi tempora.</li>
  </ul>
  <div class="btn specials">Specials</div>
</section>

<section class="doctor">
  <div class="doctor-photo" role="img" aria-label="Photo of a smiling senior doctor in a white coat with stethoscope"></div>
  <h2>Meet Our Doctor</h2>
  <p>Sed ut perspiciatis unde omnis iste natus error sit voluptatem accusantium doloremque laudantium, totam rem eaque ipsa quae ab illo inventore veritatis et quasi architecto beatae vitae dicta sunt explicabo. Nemo enim ipsam voluptatem quia voluptas sit aspernatur aut odit aut fugit, sed quia consequuntur magni dolores eos qui ratione voluptatem sequi nesciunt. Neque porro quisquam est, qui dolorem ipsum quia dolor sit amet, consectetur, adipisci velit, sed quia non numquam eius modi tempora incidunt ut labore et dolore magnam aliquam quaerat voluptatem. Ut enim ad minima veniam, quis nostrum exercitationem ullam corporis suscipit laboriosam, nisi ut aliquid ex ea commodi consequatur? Quis autem vel eum iure reprehenderit qui in ea voluptate velit esse quam nihil molestiae consequatur...</p>
  <div class="btn meet-btn">Meet Dr Whitfield</div>
</section>

<section class="partners" aria-label="Professional memberships">
  <div class="badge" style="left:105px;width:110px;border-radius:4px"></div>
  <div class="badge" style="left:300px;width:60px;border-radius:4px"></div>
  <div class="badge" style="left:446px;width:160px;border-radius:4px"></div>
  <div class="badge" style="left:676px;width:80px;border-radius:4px"></div>
  <div class="badge" style="left:828px;width:68px;border-radius:50%"></div>
  <div class="badge" style="left:986px;width:114px;border-radius:4px"></div>
</section>

<footer class="footer">
  <h4 style="left:98px">Face</h4>
  <div class="col" style="left:98px">Facelift<br>Eyelid Surgery<br>Brow Lift Surgery<br>Rhinoplasty Surgery</div>
  <div class="col" style="left:235px">Otoplasty Surgery<br>Laser Resurfacing<br>Chin Enlargement</div>
  <h4 style="left:425px">Body</h4>
  <div class="col" style="left:425px">Tummy Tuck<br>Liposuction<br>Brachioplasty</div>
  <h4 style="left:596px">Breast</h4>
  <div class="col" style="left:596px">Breast Augmentation<br>Breast Reduction<br>Breast Lift<br>Breast Reconstruction</div>
  <h4 style="left:808px">Our Clinics</h4>
  <div class="col" style="left:808px">Bayview<br>512 Coastline Rd, Suite 18<br>Bayview, NSW 2104<br>Elmsford</div>
  <div class="col" style="left:980px">Tel: 02 9000 4821<br>Port Allen<br>7/4 Carrow St<br>Westhaven, NSW 2290</div>
  <div class="divider"></div>
  <div class="copy">Copyrights © harbourlinecosmetic .2016 | Allrights reserved.</div>
  <div class="connect">Connect with us:</div>
  <div class="social" style="left:937px"></div>
  <div class="social" style="left:967px"></div>
  <div class="social" style="left:997px"></div>
  <div class="social" style="left:1027px"></div>
  <div class="social" style="left:1057px"></div>
  <div class="code">C11</div>
</footer>

</body>
</html>
```